Lend a Lantern Website Design (design layout only)

We need a website design for a new nonprofit organization based in Des Moines, Iowa called Lend a Lantern. The nonprofit provides soccer training opportunities to youth soccer players looking to improve their game while also affecting the lives of the less fortunate in a positive way. While participating in the training programs the players also go out and raise money for selected charities. The organization then donates the funds. In its first 18 months we donated $10,500. We would like to see designs attempt to symbolize the mission of the nonprofit - essentially "improve you while improving someone else."

We would like to see the following features:

· A place to donate - Our intent is to have the home page linked to the donation page; a simple straight-forward process for people to give money, and make donating as painless as possible - no account needed to make a donation, credit card or e-check should be the only information needed to donate, and have it be on a single page.

· A photo gallery so people can browse the photo gallery to get a better understanding of our organization and a place to add videos and a calendar to show upcoming events

· A place for contact information and the profiles of directors and board members. This should include a spot showing all the charities the organization donates to. Also includes a news section/blog for comments and suggestions.

We want the design to revolve around the content and mission. We would really like to stress our organization as nonprofit. We would also like if the website was user friendly and easy to navigate.

The logo of our organization is uploaded

```html
<!DOCTYPE html>
<html lang="en">
<head>
<meta charset="utf-8">
<title>Lend a Lantern</title>
<link href="https://fonts.googleapis.com/css2?family=Source+Sans+3:wght@400;600;700&display=swap" rel="stylesheet">
<style>
:root{
  --green-dark:#2f4a18;
  --green-deep:#1c2a0f;
  --green:#3f6a24;
  --green-light:#7fa250;
  --green-mid:#5d7c36;
  --charcoal:#333333;
  --black:#1a1a1a;
  --text:#666666;
  --heading:#333333;
  --orange:#e2661a;
  --brown:#4a2e1a;
  --line:#dddddd;
  --field:#f0f0f0;
}
*{box-sizing:border-box;margin:0;padding:0}
html,body{width:826px;height:1200px;overflow:hidden;background:#fff}
body{font-family:"Source Sans 3",sans-serif;color:var(--text);position:relative}
.abs{position:absolute}

.brand{left:90px;top:16px;display:flex;align-items:center;gap:8px}
.brand-mark{width:30px;height:30px;background:var(--green-light);border-radius:50%}
.brand-name{font-size:24px;font-weight:700;color:var(--green-light);line-height:1}
.follow{left:485px;top:27px;display:flex;align-items:center;gap:6px;font-size:11px;color:#444}
.social{width:16px;height:16px;border-radius:50%;background:var(--green-mid)}
.account{left:652px;top:24px;width:71px;height:20px;background:#ddd;font-size:9.5px;color:#555;display:flex;align-items:center;justify-content:center}

.nav{left:83px;top:67px;width:667px;height:27px;background:var(--green-dark);display:flex;align-items:center}
.nav-item{color:#fff;font-size:11px;padding:0 0 0 13px;display:flex;align-items:center;gap:14px}
.nav-item+.nav-item::before{content:"";width:4px;height:4px;border-radius:50%;background:#fff;margin-right:6px;margin-left:-8px}
.search{margin-left:auto;width:130px;height:27px;background:var(--green-deep);display:flex;align-items:center;justify-content:space-between;padding:0 7px;font-size:8px;color:#777}

.hero{left:84px;top:105px;width:662px;height:299px;background:linear-gradient(180deg,#9c9e98 0%,#8a8e80 45%,#5f7a3e 70%,#4d6a30 100%)}
.caption{left:101px;top:186px;width:310px;height:148px;background:rgba(30,30,30,.72);padding:14px 11px;color:#fff}
.caption h1{font-size:23px;font-weight:600;line-height:1.15}
.caption h2{font-size:19px;font-weight:600;line-height:1.4}
.caption p{font-size:8.5px;line-height:1.5;margin-top:5px}
.btn{display:inline-block;background:var(--green);color:#fff;font-size:11px;padding:5px 12px}
.caption .btn{margin-top:10px;padding:6px 13px}
.dots{left:681px;top:372px;display:flex;gap:6px}
.dot{width:9px;height:9px;border-radius:50%;background:#222;border:1px solid #fff}
.dot.on{background:#eee}

.about{left:89px;top:416px;width:480px}
.about h3{font-size:14px;font-weight:700;color:var(--heading);margin-bottom:8px}
.about p{font-size:9px;line-height:1.55}
.about .btn{margin-top:9px;padding:6px 8px;font-size:11.5px}

.cta{left:584px;width:163px;height:62px;color:#fff;padding:10px 7px;display:flex;justify-content:space-between;align-items:center}
.cta h4{font-size:18px;font-weight:600;line-height:1}
.cta p{font-size:9px;line-height:1.3;margin-top:3px}
.cta-icon{width:34px;height:34px;border-radius:50%;flex:none}
.give{top:416px;background:var(--green-light)}
.give .cta-icon{background:var(--green-mid);border:2px solid #9bb873}
.help{top:483px;background:var(--green-mid)}
.help .cta-icon{background:#2a3a18}
.donate{top:550px;background:var(--charcoal)}
.donate .cta-icon{background:#000;border:2px solid #fff}

.card{top:633px;width:207px;height:176px;border:1px solid #e4e4e4;border-top:none}
.card-head{height:32px;background:linear-gradient(180deg,#2b2b2b,#000);color:#fff;font-size:14px;font-weight:700;padding:7px 9px}
.card-media{margin:16px 8px 0;height:85px}
.card-rule{margin:12px 8px 0;border-top:1px solid var(--line)}
.card-link{position:absolute;right:7px;bottom:10px;font-size:8.5px;color:var(--orange)}

.gallery-title{left:0;width:826px;top:826px;text-align:center;font-size:21px;font-weight:600;color:var(--brown)}
.gallery-sub{left:0;width:826px;top:857px;text-align:center;font-size:12px;color:#555}
.thumb{top:884px;width:151px;height:112px;border:1px solid #ccc}
.arrow{top:915px}

.donation{left:83px;top:1012px;width:663px;height:148px;border:1px solid #e6e6e6;padding:0 14px}
.donation h5{position:absolute;left:14px;top:8px;font-size:15px;font-weight:400;color:#333}
.donation .note{position:absolute;right:17px;top:14px;font-size:8.5px;color:#333}
.donation .rule{position:absolute;left:14px;right:17px;top:32px;border-top:1px solid #eee}
.label{position:absolute;font-size:8px;color:#333}
.field{position:absolute;background:var(--field);border:1px solid #e2e2e2;height:21px;font-size:8px;color:#444;padding:0 6px;display:flex;align-items:center}
.select-btn{position:absolute;right:0;top:0;width:24px;height:21px;background:var(--green-dark);display:flex;align-items:center;justify-content:center}
.radio-row{position:absolute;left:16px;top:116px;display:flex;gap:12px;font-size:8px;color:#666}
.radio{display:flex;align-items:center;gap:5px}
.radio i{width:7px;height:7px;border-radius:50%;border:1px solid #ccc}
.ccv-help{position:absolute;left:319px;top:114px;font-size:7px;color:#777;line-height:1.4}
.ccv-help u{color:#555}

.footer{left:83px;top:1176px;width:667px;height:24px;background:var(--charcoal);color:#fff;font-size:8.5px;display:flex;align-items:center;justify-content:space-between;padding:0 14px 0 7px}
</style>
</head>
<body>

<div class="abs brand"><span class="brand-mark"></span><span class="brand-name">Lend a Lantern</span></div>
<div class="abs follow">Follow us on:
  <span class="social"></span><span class="social"></span><span class="social"></span><span class="social"></span>
</div>
<div class="abs account">My Account (log in)</div>

<nav class="abs nav">
  <span class="nav-item">HOME</span>
  <span class="nav-item">ABOUT US</span>
  <span class="nav-item">TEAM</span>
  <span class="nav-item">HELP</span>
  <span class="nav-item">LEAD</span>
  <span class="nav-item">GALLERY</span>
  <span class="nav-item">CONTACT US</span>
  <div class="search">SEARCH HERE
    <svg width="11" height="11" viewBox="0 0 12 12"><circle cx="5" cy="5" r="3.8" fill="none" stroke="#fff" stroke-width="1.8"/><line x1="8" y1="8" x2="11" y2="11" stroke="#fff" stroke-width="2"/></svg>
  </div>
</nav>

<div class="abs hero" role="img" aria-label="Youth soccer players running after a ball on a grass field"></div>
<div class="abs caption">
  <h1>Every Child Matters</h1>
  <h2>Everyone Can Make A Difference</h2>
  <p>Sed ut perspiciatis unde omnis iste natus error sit voluptatem accusan-<br>tium doloremque laudantium, totam rem aperiam, eaque ipsa quae ab</p>
  <span class="btn">LEARN MORE</span>
</div>
<div class="abs dots"><span class="dot on"></span><span class="dot"></span><span class="dot"></span><span class="dot"></span></div>

<section class="abs about">
  <h3>ABOUT OUR COMPANY</h3>
  <p>Sed ut perspiciatis unde omnis iste natus error sit voluptatem accusantium doloremque laudantium, totam rem aperiam, eaque ipsa quae ab illo inventore veritatis et quasi architecto beatae vitae dicta sunt explicabo. Nemo enim ipsam voluptatem quia voluptas sit aspernatur aut odit aut fugit, sed quia consequuntur magni dolores eos qui ratione voluptatem sequi nesciunt. Neque<br>&nbsp;porro quisquam est, qui dolorem ipsum quia dolor sit amet, consectetur, adipisci velit, sed quia non numquam eius<br>&nbsp;modi tempora incidunt ut labore et dolore magnam aliquam quaerat voluptatem. Ut enim ad minima veniam, quis nostrum<br>&nbsp;exercitationem ullam corporis suscipit laborio</p>
  <span class="btn">LEARN MORE</span>
</section>

<div class="abs cta give"><div><h4>Give</h4><p>Send a Share Package</p></div><span class="cta-icon"></span></div>
<div class="abs cta help"><div><h4>Help</h4><p>Join a Give Event<br>near you</p></div><span class="cta-icon"></span></div>
<div class="abs cta donate"><div><h4>Donate now</h4><p>Donaet for the children<br>and ger &nbsp;love</p></div><span class="cta-icon"></span></div>

<div class="abs card" style="left:83px">
  <div class="card-head">UPCOMING EVENTS</div>
  <div class="card-media" style="background:linear-gradient(135deg,#e8e4dc,#d8d4cc 60%,#e4c8c0)" role="img" aria-label="Red pin placed on a road map"></div>
  <div class="card-rule"></div>
  <span class="card-link">View all events</span>
</div>
<div class="abs card" style="left:313px">
  <div class="card-head">LATEST NEWS</div>
  <div class="card-media" style="background:linear-gradient(180deg,#d8ecf4,#8cbf5c 60%,#5c9a34)" role="img" aria-label="Young player kicking a soccer ball"></div>
  <div class="card-rule"></div>
  <span class="card-link">View all News</span>
</div>
<div class="abs card" style="left:541px">
  <div class="card-head">OUR VIDEOS</div>
  <div class="card-media" style="height:94px;background:linear-gradient(180deg,#8e8e86,#6f7a58 50%,#4e6a2c)" role="img" aria-label="Video still of children playing soccer">
    <svg width="100%" height="94" viewBox="0 0 188 94"><rect x="78" y="33" width="32" height="28" rx="4" fill="rgba(255,255,255,.7)"/><polygon points="89,40 89,54 101,47" fill="#3f6a24"/></svg>
  </div>
  <div class="card-rule"></div>
  <span class="card-link">View all Videos</span>
</div>

<div class="abs gallery-title">Gallery</div>
<div class="abs gallery-sub">Click Image To Enlarge</div>
<svg class="abs arrow" style="left:82px" width="12" height="42" viewBox="0 0 12 42"><polygon points="11,0 1,21 11,42 6,21" fill="#a8a890"/></svg>
<div class="abs thumb" style="left:105px;background:linear-gradient(180deg,#5a7030,#6f8c38 60%,#8aa850)" role="img" aria-label="Soccer ball on grass with players behind"></div>
<div class="abs thumb" style="left:262px;background:linear-gradient(180deg,#4a6a2a,#7ea040)" role="img" aria-label="Two young players chasing a ball"></div>
<div class="abs thumb" style="left:420px;background:linear-gradient(180deg,#5a7a30,#8ab048)" role="img" aria-label="Youth players in blue and yellow kits"></div>
<div class="abs thumb" style="left:578px;background:linear-gradient(180deg,#d8ecf4,#9ccc6c 60%,#6aa83c)" role="img" aria-label="Boy kicking a ball in a park"></div>
<svg class="abs arrow" style="left:738px" width="12" height="42" viewBox="0 0 12 42"><polygon points="1,0 11,21 1,42 6,21" fill="#a8a890"/></svg>

<section class="abs donation">
  <h5>Donation Details</h5>
  <span class="note">Lorem ipsum dolor *</span>
  <div class="rule"></div>

  <span class="label" style="left:14px;top:43px">Donation Amount *</span>
  <div class="field" style="left:15px;top:57px;width:189px">$0.00 Per month<span class="select-btn"><svg width="9" height="6"><polygon points="0,0 9,0 4.5,6" fill="#fff"/></svg></span></div>

  <span class="label" style="left:246px;top:43px">Name on card *</span>
  <div class="field" style="left:246px;top:57px;width:188px"></div>

  <span class="label" style="left:458px;top:43px">Credit card number *</span>
  <div class="field" style="left:458px;top:57px;width:188px"></div>

  <span class="label" style="left:14px;top:96px">Select your credit card type *</span>
  <div class="radio-row">
    <span class="radio"><i></i>Cardline</span>
    <span class="radio"><i></i>Amplex</span>
    <span class="radio"><i></i>Dinewell</span>
  </div>

  <span class="label" style="left:247px;top:96px">CCV number *</span>
  <div class="field" style="left:246px;top:110px;width:70px"></div>
  <div class="ccv-help">What is CCV ?<br><u>Click here</u></div>

  <span class="label" style="left:460px;top:98px">Expiry date *</span>
  <div class="field" style="left:460px;top:111px;width:82px;background:#fff">Jan<span class="select-btn"><svg width="9" height="6"><polygon points="0,0 9,0 4.5,6" fill="#fff"/></svg></span></div>
  <div class="field" style="left:560px;top:111px;width:82px;background:#fff">2014<span class="select-btn"><svg width="9" height="6"><polygon points="0,0 9,0 4.5,6" fill="#fff"/></svg></span></div>
</section>

<footer class="abs footer">
  <span>Copyrights © 2014 lend a lantern - All Rights Reserved</span>
  <span>Privacy Policy &nbsp; | &nbsp; Terms Of Uses</span>
</footer>

</body>
</html>
```